Heron valley RV Resort business card

I need a design card for the logo I just had made on here. I will provide it and please make some cool designs, thank you.

I would like the card to have
- phone number (865-318-2967)
- email ( heronvalleyrv@pinemail.com)
- address to the park ( 5186 Quarry Gate Loop rd, Maryville, TN) ZIP: 37429
on the back for double sided id like some lines for writing on. thanks

please follow the logo we provided in the files, I can provide the photoshop file if you need it.

please note this is in the Smokey mountains of Tennessee

Target Market(s)

cabin/rv rentals

Industry/Entity Type

rv/campground/cabin rentals

Contact Information for Business Card

address/email/phone number I added details in brief

Requirements
Must have
• on the back add a bear or something cool

```html
<!DOCTYPE html>
<html lang="en">
<head>
<meta charset="utf-8">
<title>Heron Valley RV Resort – Business Card</title>
<link rel="stylesheet" href="https://fonts.googleapis.com/css2?family=Playfair+Display:wght@400;600&family=Arimo:wght@400&display=swap">
<style>
  :root {
    --page-bg: #e4e4e4;
    --card-bg: #f7f7f7;
    --ink: #1b1b1b;
    --rule: #3a3a3a;
    --card-shadow: rgba(0, 0, 0, 0.14);
  }
  * { box-sizing: border-box; margin: 0; padding: 0; }
  html, body {
    width: 1200px;
    height: 930px;
    overflow: hidden;
    background: var(--page-bg);
  }
  .sheet {
    position: relative;
    width: 1200px;
    height: 930px;
  }
  .card {
    position: absolute;
    top: 310px;
    width: 540px;
    height: 309px;
    background: var(--card-bg);
    box-shadow: 0 6px 18px var(--card-shadow);
    color: var(--ink);
  }
  .card--front { left: 40px; }
  .card--back { left: 620px; }

  /* Front */
  .brand-mark {
    position: absolute;
    left: 300px;
    top: 40px;
    width: 200px;
    display: flex;
    flex-direction: column;
    align-items: center;
    gap: 12px;
  }
  .brand-mark__circle {
    width: 62px;
    height: 62px;
    border-radius: 50%;
    border: 2px solid var(--ink);
  }
  .brand-mark__name {
    font-family: "Playfair Display", serif;
    font-weight: 600;
    font-size: 19px;
    letter-spacing: 0.04em;
    text-transform: uppercase;
    text-align: center;
    line-height: 1.25;
    color: var(--ink);
  }
  .contact {
    position: absolute;
    left: 24px;
    right: 24px;
    top: 215px;
    display: flex;
    align-items: center;
    justify-content: center;
    gap: 16px;
    font-family: "Arimo", sans-serif;
    font-size: 14px;
    line-height: 1.45;
  }
  .contact__direct { text-align: right; }
  .contact__divider {
    width: 1px;
    height: 42px;
    background: var(--rule);
  }
  .contact__line {
    display: flex;
    align-items: center;
    gap: 6px;
  }
  .contact__direct .contact__line { justify-content: flex-end; }
  .contact__address { display: flex; gap: 6px; align-items: flex-start; }
  .icon { width: 12px; height: 12px; flex: none; }

  /* Back */
  .back-title {
    position: absolute;
    left: 0;
    right: 0;
    top: 52px;
    text-align: center;
    font-family: "Playfair Display", serif;
    font-weight: 400;
    font-size: 34px;
    letter-spacing: 0.06em;
    text-transform: uppercase;
  }
  .writing-lines {
    position: absolute;
    left: 70px;
    right: 70px;
    top: 150px;
    display: flex;
    flex-direction: column;
    gap: 36px;
  }
  .writing-lines__rule {
    height: 1px;
    background: var(--rule);
  }
</style>
</head>
<body>
<main class="sheet">
  <section class="card card--front" aria-label="Front of business card">
    <div class="brand-mark">
      <span class="brand-mark__circle"></span>
      <span class="brand-mark__name">Heron Valley<br>RV Resort</span>
    </div>
    <div class="contact">
      <div class="contact__direct">
        <div class="contact__line">
          <span>(865-318-2967)</span>
          <svg class="icon" viewBox="0 0 24 24" aria-hidden="true"><path fill="#1b1b1b" d="M6.6 10.8a15.1 15.1 0 0 0 6.6 6.6l2.2-2.2c.3-.3.7-.4 1-.2 1.1.4 2.3.6 3.6.6.6 0 1 .4 1 1V20c0 .6-.4 1-1 1A17 17 0 0 1 3 4c0-.6.4-1 1-1h3.5c.6 0 1 .4 1 1 0 1.3.2 2.5.6 3.6.1.3 0 .7-.2 1z"/></svg>
        </div>
        <div class="contact__line">
          <span>heronvalleyrv@pinemail.com</span>
          <svg class="icon" viewBox="0 0 24 24" aria-hidden="true"><path fill="#1b1b1b" d="M2 5h20v14H2zm2 2v.4l8 5.3 8-5.3V7zm0 2.8V17h16V9.8l-8 5.3z"/></svg>
        </div>
      </div>
      <span class="contact__divider"></span>
      <div class="contact__address">
        <svg class="icon" viewBox="0 0 24 24" aria-hidden="true" style="margin-top:3px"><path fill="#1b1b1b" d="M12 2a7 7 0 0 0-7 7c0 5 7 13 7 13s7-8 7-13a7 7 0 0 0-7-7zm0 9.5A2.5 2.5 0 1 1 12 6.5a2.5 2.5 0 0 1 0 5z"/></svg>
        <div>
          <div>5186 Quarry Gate Loop rd</div>
          <div>Maryville, TN. ZIP: 37429</div>
        </div>
      </div>
    </div>
  </section>

  <section class="card card--back" aria-label="Back of business card">
    <h1 class="back-title">Heron Valley</h1>
    <div class="writing-lines">
      <span class="writing-lines__rule"></span>
      <span class="writing-lines__rule"></span>
      <span class="writing-lines__rule"></span>
    </div>
  </section>
</main>
</body>
</html>
```